UPliften website redesign to provide information about experiential workshops, film work and other

We need a redesign of our website upliften.org. We conduct experiential workshops of discovery and transformation for individuals and organizations. We need the website to reflect the full extent of UPliften programs, and be an information hub for UPliften workshops and communities as they develop.

The attached documents contain information about the organization - it's brandbook, copy for web pages, a website layout and a couple of images.

The site is for individuals and companies looking to promote and be change to make a difference. It should be warm, welcoming, and create excitement around the concepts and the ability to discover a new way of being in the world. We are about creating communities around the globe who will embody play, freedom, curiosity and expanded possibilities. We are creating a space for this to happen, both physically (workshops) and online.

We will be on either a BrightPanel, but mos tlikely a Zantro plaform.

Please look at the current site at www.upliften.org

Target Market(s)

Initially, are target market will be baby boomers, but will expand to include millennials and students.

Coding

Coded - Design and coding required

Number of Pages Required

5+ page

Requirements
Must have
• The colors, logo and fonts from the brand book.
Nice to have
• Complimentary use of brand colors to create an attractive presentation and energy

```html
<!DOCTYPE html>
<html lang="en">
<head>
<meta charset="utf-8">
<title>UPliften — Workshops of Discovery and Transformation</title>
<link href="https://fonts.googleapis.com/css2?family=Montserrat:wght@400;500;600;700;800&family=Hind:wght@400;500&display=swap" rel="stylesheet">
<style>
:root{
  --orange:#eca24d;
  --green:#7dbf85;
  --mauve:#a76e77;
  --coral:#e8613c;
  --teal:#7fc6c1;
  --gold:#d29a4b;
  --ink:#1d1d1d;
  --text:#3a3a3a;
  --light:#ffffff;
  --rule:#d9d9d9;
  --footer:#222222;
}
*{box-sizing:border-box;margin:0;padding:0}
html,body{width:1200px;height:3593px;overflow:hidden}
body{font-family:"Montserrat",sans-serif;color:var(--text);background:var(--light);position:relative}
section,header,footer{position:absolute;left:0;width:1200px}

/* Hero */
.hero{top:0;height:640px;background:linear-gradient(180deg,#3b4136 0%,#4f5346 45%,#2b2d29 100%)}
.hero-photo{position:absolute;inset:0;background:radial-gradient(ellipse at 30% 45%,#7b7467 0%,rgba(0,0,0,0) 45%),radial-gradient(ellipse at 65% 45%,#7c7a70 0%,rgba(0,0,0,0) 40%)}
.brand{position:absolute;left:100px;top:42px;display:flex;align-items:center;gap:12px;color:var(--light);font-weight:800;font-size:34px;letter-spacing:4px}
.brand-mark{width:22px;height:22px;border:3px solid var(--light)}
.top-actions{position:absolute;right:100px;top:38px;display:flex;gap:18px}
.btn{display:inline-block;font-weight:600;font-size:15px;color:var(--light);text-transform:uppercase;padding:8px 20px;text-decoration:none}
.btn-orange{background:var(--orange)}
.btn-green{background:var(--green)}
.nav{position:absolute;left:100px;right:100px;top:114px;border-top:1px solid rgba(255,255,255,.5);display:flex;justify-content:space-between;padding:20px 10px 0}
.nav a{color:var(--light);font-weight:600;font-size:15px;text-decoration:none;text-transform:uppercase}
.hero-q{position:absolute;bottom:0;width:600px;height:200px;display:flex;align-items:center;justify-content:center;text-align:center;color:var(--light);font-weight:700;font-size:33px;line-height:1.6;text-transform:uppercase}
.hero-q.left{left:0;background:rgba(0,0,0,.45)}
.hero-q.right{left:600px;background:rgba(0,0,0,.3)}

/* Discover */
.discover{top:640px;height:720px}
.section-title{text-align:center;color:var(--ink);font-weight:700;font-size:32px;line-height:1.6;text-transform:uppercase}
.discover .section-title{margin-top:92px}
.tiles{position:absolute;left:100px;top:253px;width:1000px;height:350px;display:grid;grid-template-columns:repeat(4,250px);grid-template-rows:repeat(2,175px)}
.tile{position:relative;display:flex;flex-direction:column;align-items:center;justify-content:center;text-align:center;color:var(--light);font-weight:700;font-size:21px;line-height:1.75;text-transform:uppercase;padding:0 12px}
.tile.small{font-size:18px}
.tile p{font-family:"Hind",sans-serif;font-weight:400;font-size:13px;text-transform:none;line-height:1.5;margin-top:10px}
.t-green{background:var(--green)}
.t-mauve{background:var(--mauve)}
.t-orange{background:var(--orange)}
.t-coral{background:var(--coral)}
.t-green::after,.t-coral::before{content:"";position:absolute;left:50%;margin-left:-10px;border:10px solid transparent}
.t-green::after{bottom:-20px;border-top-color:var(--green);z-index:2}
.t-coral::before{top:-20px;border-bottom-color:var(--coral);z-index:2}
.ph-flowers{background:linear-gradient(135deg,#b7a4b9,#8f7a92)}
.ph-hands{background:linear-gradient(135deg,#2f5b5a,#7fa9a5 60%,#264544)}
.ph-lamp{background:linear-gradient(160deg,#4a4e57,#2d3038)}
.ph-lights{background:radial-gradient(circle at 50% 70%,#f3c98a,#d7994d 70%)}

/* Vision */
.vision{top:1360px;height:408px;background:var(--orange)}
.vision-photo{position:absolute;left:0;top:0;width:558px;height:408px;background:linear-gradient(150deg,#6d7a5c,#3c3a33 60%,#2a2824)}
.vision-body{position:absolute;left:615px;top:45px;width:500px;color:var(--light)}
.vision-body h2{font-weight:700;font-size:31px;text-transform:uppercase;margin-bottom:20px}
.vision-body p{font-family:"Hind",sans-serif;font-size:13px;line-height:1.8;margin-bottom:18px}
.vision-body b{font-weight:500}
.btn-outline{border:2px solid var(--light);font-size:14px;padding:8px 18px;margin-top:8px}

/* What we do */
.what{top:1768px;height:700px}
.what .section-title{margin-top:100px}
.what-intro{width:820px;margin:22px auto 0;text-align:center;font-family:"Hind",sans-serif;font-size:13px;line-height:2}
.what-sub{width:420px;margin:22px auto 0;text-align:center;font-weight:500;font-size:19px;line-height:1.6;color:var(--text)}
.movements{position:absolute;left:100px;top:378px;width:1000px;display:flex;justify-content:space-between}
.movement{width:186px;height:192px;border:1px solid #e2e2e2;box-shadow:0 2px 6px rgba(0,0,0,.12);display:flex;flex-direction:column;align-items:center;padding-top:34px;text-align:center;font-family:"Hind",sans-serif;font-weight:500;font-size:25px;line-height:1;color:var(--ink)}
.movement-mark{width:64px;height:64px;border-radius:50%;margin:4px 0 22px;opacity:.85}
.m-coral{background:var(--coral)}
.m-teal{background:var(--teal)}
.m-gold{background:var(--gold)}
.m-green{background:var(--green)}
.m-mauve{background:var(--mauve)}
.divider{position:absolute;left:100px;top:675px;width:1000px;border-top:2px solid var(--rule)}

/* Stirring the Calm */
.calm{top:2468px;height:564px}
.calm h2{position:absolute;left:98px;top:68px;font-weight:700;font-size:33px;color:var(--ink);text-transform:uppercase}
.calm-copy{position:absolute;left:100px;top:152px;width:520px;font-family:"Hind",sans-serif;font-size:13px;line-height:1.9}
.calm-copy p{margin-bottom:20px}
.calm-copy b{font-weight:500;color:var(--ink)}
.calm .btn-green{position:absolute;left:100px;top:413px;padding:11px 28px;font-size:15px}
.calm-frame{position:absolute;left:728px;top:75px;width:426px;height:312px;border:2px solid var(--mauve)}
.calm-photo{position:absolute;left:670px;top:135px;width:428px;height:316px;background:linear-gradient(160deg,#8aa5a7,#5f7c80 55%,#4b6467)}

/* Community */
.community{top:3032px;height:460px;background:linear-gradient(180deg,#e6623d,#dd5a37)}
.community h2{text-align:center;color:var(--light);font-weight:700;font-size:30px;margin-top:68px;text-transform:uppercase}
.community-intro{width:560px;margin:12px auto 0;text-align:center;color:var(--light);font-family:"Hind",sans-serif;font-size:12px;line-height:1.7}
.form{position:absolute;left:200px;top:187px;width:800px}
.form-row{display:flex;gap:16px;margin-bottom:17px}
.field{flex:1;height:42px;background:var(--light);font-family:"Hind",sans-serif;font-size:12px;color:#555;padding:12px 18px}
.field.message{height:72px}
.form .btn-green{display:block;width:156px;margin:22px auto 0;text-align:center;padding:11px 0;font-size:15px}

/* Footer */
.footer{top:3492px;height:101px;background:var(--footer);color:var(--light)}
.footer small{position:absolute;left:100px;top:42px;font-weight:600;font-size:14px}
.social{position:absolute;left:903px;top:30px;display:flex;gap:13px}
.social span{width:40px;height:40px;border-radius:50%;background:var(--light);display:block}
</style>
</head>
<body>

<header class="hero">
  <div class="hero-photo" role="img" aria-label="Photo of two workshop leaders speaking to a group in a wooded room"></div>
  <div class="brand"><span class="brand-mark"></span>UPLIFTEN</div>
  <div class="top-actions">
    <a class="btn btn-orange" href="#">Email Capture</a>
    <a class="btn btn-green" href="#">Member Login</a>
  </div>
  <nav class="nav">
    <a href="#">About Us</a><a href="#">Workshops</a><a href="#">UPliften Projects</a><a href="#">Films</a><a href="#">Store &amp; Resources</a><a href="#">Community</a><a href="#">Contact Us</a>
  </nav>
  <div class="hero-q left">What world do we<br>want to live in?</div>
  <div class="hero-q right">What kind of life do you<br>want to create?</div>
</header>

<section class="discover">
  <h2 class="section-title">Discover an opportunity to live a more<br>dynamic and meaningful life</h2>
  <div class="tiles">
    <div class="tile ph-flowers" role="img" aria-label="Photo of dried flowers in soft violet tones"></div>
    <div class="tile t-green">Creates<br>opportunities<br>for connecting</div>
    <div class="tile ph-hands" role="img" aria-label="Photo of hands reaching into water and leaves"></div>
    <div class="tile t-mauve">Provides<br>opportunities for<br>collaboration<br>&amp; creation</div>
    <div class="tile t-orange small">Moves Energy<p>Nemo enim ipsam voluptatem quia voluptas sit aspernatur aut odit aut fugit sed quia consequuntur.</p></div>
    <div class="tile ph-lamp" role="img" aria-label="Photo of a telescope against a dark sky"></div>
    <div class="tile t-coral">Deepens<br>experience of<br>our life</div>
    <div class="tile ph-lights" role="img" aria-label="Photo of a person standing under warm strings of light"></div>
  </div>
</section>

<section class="vision">
  <div class="vision-photo" role="img" aria-label="Photo of a workshop group seated in a circle in a wooden lodge"></div>
  <div class="vision-body">
    <h2>Our Vision</h2>
    <p>We <b>envision a world</b> in which all people and communities can challenge and <b>break free</b> from stories that no longer serve us. We believe that solutions to contemporary challenges will emerge from a place of curiosity, love and connection.</p>
    <p>Through inspiration, <b>conscious reflection</b>, and collaboration, we <b>take responsibility</b> for the world <b>we are manifesting</b>, and we can discover and create new possibilities for the lives and the society we desire to build.</p>
    <a class="btn btn-outline" href="#">Read More &#10140;</a>
  </div>
</section>

<section class="what">
  <h2 class="section-title">What we do</h2>
  <p class="what-intro">UPliften Life is a workshop designed to re-engage you with life. Through interactive exercises and personal exploration, you are taken on a journey that ultimately leaves you experiencing life as a Creator. You will learn to see beliefs and patterns that hold you back in work and relationships as well as a path to transforming the story of your life.</p>
  <p class="what-sub">UPliften Life is a 2-3 day workshop experienced in 5 movements:</p>
  <div class="movements">
    <div class="movement"><span class="movement-mark m-coral" role="img" aria-label="Symbol for the Curiosity movement"></span>Curiosity</div>
    <div class="movement"><span class="movement-mark m-teal" role="img" aria-label="Symbol for the Awareness movement"></span>Awareness</div>
    <div class="movement"><span class="movement-mark m-gold" role="img" aria-label="Symbol for the Owning Your Creation movement"></span>Owning Your<br>Creation</div>
    <div class="movement"><span class="movement-mark m-green" role="img" aria-label="Symbol for the Reimagining movement"></span>Reimaining</div>
    <div class="movement"><span class="movement-mark m-mauve" role="img" aria-label="Symbol for the Manifesting movement"></span>Manifesting</div>
  </div>
  <div class="divider"></div>
</section>

<section class="calm">
  <h2>Stirring the Calm</h2>
  <div class="calm-copy">
    <p>The Stirring the Calm workshop—an extension of the documentary of the same name—is an <b>experiential</b> process to transform participants into disturbers of the status quo within themselves, to <b>enhance</b> their relationships with others, and to change the environments in which they exist—and ultimately society—for the better.</p>
    <p>This workshop experience <b>challenges</b> us all to understand the narratives we live within, to <b>look at our current roles</b> in society, and to decide what role we will play to create a more humane, just and <b>peaceful world</b>, for all. It all starts with our <b>willingness</b> to disturb the “calm” of the status quo.</p>
  </div>
  <a class="btn btn-green" href="#">Join Us Now</a>
  <div class="calm-frame"></div>
  <div class="calm-photo" role="img" aria-label="Photo of a crowd and costumed performers in a street parade"></div>
</section>

<section class="community">
  <h2>In Your Community</h2>
  <p class="community-intro">Bring UPliften or the Stirring the Calm workshop to your community. We would love to hear from you. Please fill out the brief form here.</p>
  <div class="form">
    <div class="form-row"><div class="field">Enter Name</div><div class="field">Email Address</div><div class="field">Phone</div></div>
    <div class="form-row"><div class="field message">Message</div></div>
    <a class="btn btn-green" href="#">Submit Now</a>
  </div>
</section>

<footer class="footer">
  <small>© Copyright 2018 UPliften. All Rights Reserved.</small>
  <div class="social"><span></span><span></span><span></span><span></span></div>
</footer>

</body>
</html>
```